Valmoric Pocket Folder

Create a new pocket folder
An Overview / Background of the Business & Services
We would like a new folder to use when making formal presentations
* The Target Market / Audience you are trying to reach
The target audience are commercial businesses that we are selling group insurance products to
* Design Specifics; any preferences or ideas for Style, Colour, Imagery, etc
We wanted to use the Houston, Texas skyline and create something that was simple, yet modern.
* Do you have an existing website or Facebook page were designers can learn more about your company?
Yes, http://www.valmoriccorp.example and we are on Linked-In.

```html
<!DOCTYPE html>
<html lang="en">
<head>
<meta charset="utf-8">
<title>Valmoric Pocket Folder</title>
<link rel="stylesheet" href="https://fonts.googleapis.com/css2?family=Source+Sans+3:wght@400;700&display=swap">
<style>
  :root {
    --stage: #b8b8b8;
    --slate: #5b5c60;
    --slate-dark: #4a4b4f;
    --brand-blue: #1f95da;
    --brand-blue-mid: #1479bd;
    --brand-blue-deep: #0b5d99;
    --paper: #ffffff;
    --paper-shade: #ececec;
    --skyline: #cfd3d7;
    --skyline-soft: #dde4ea;
    --ink-light: #d9dadc;
    --logo-grey: #58595b;
  }
  html, body {
    margin: 0;
    padding: 0;
    width: 1200px;
    height: 828px;
    overflow: hidden;
    background: var(--stage);
    font-family: "Source Sans 3", Arial, sans-serif;
  }
  .folder-spread {
    position: absolute;
    left: 105px;
    top: 84px;
    width: 990px;
    height: 660px;
    display: flex;
    box-shadow: 0 14px 30px rgba(0,0,0,0.25);
  }
  .cover {
    position: relative;
    width: 495px;
    height: 660px;
    overflow: hidden;
  }
  /* Back cover */
  .back-cover {
    background: linear-gradient(200deg, var(--slate) 0%, var(--slate-dark) 100%);
  }
  .blue-field {
    position: absolute;
    inset: 0;
    width: 100%;
    height: 100%;
  }
  .back-contact {
    position: absolute;
    left: 34px;
    bottom: 40px;
    display: flex;
    align-items: flex-start;
    gap: 14px;
    color: var(--ink-light);
    font-size: 10.5px;
    line-height: 15px;
  }
  .back-contact .agency-name { font-weight: 700; }
  .contact-divider {
    width: 1px;
    height: 46px;
    background: var(--ink-light);
    opacity: 0.7;
  }
  .contact-lines { list-style: none; margin: 0; padding: 0; }
  .contact-lines li { display: flex; align-items: center; gap: 7px; }
  .contact-lines svg { width: 9px; height: 9px; fill: var(--ink-light); }
  /* Front cover */
  .front-cover {
    background: linear-gradient(160deg, var(--paper) 55%, var(--paper-shade) 100%);
  }
  .brand-lockup {
    position: absolute;
    left: 96px;
    top: 78px;
    display: flex;
    align-items: center;
    gap: 12px;
  }
  .brand-square {
    width: 44px;
    height: 44px;
    background: var(--brand-blue);
    border-radius: 4px;
  }
  .brand-name {
    font-size: 44px;
    font-weight: 700;
    color: var(--logo-grey);
    letter-spacing: 0.5px;
    line-height: 1;
  }
  .skyline-area {
    position: absolute;
    left: 0;
    right: 0;
    top: 230px;
    bottom: 20px;
    background:
      linear-gradient(180deg, rgba(255,255,255,0) 0%, var(--skyline-soft) 45%, var(--skyline) 100%);
    opacity: 0.9;
  }
</style>
</head>
<body>
  <main class="folder-spread">
    <section class="cover back-cover">
      <svg class="blue-field" viewBox="0 0 495 660" preserveAspectRatio="none" aria-hidden="true">
        <defs>
          <linearGradient id="blueTone" x1="0" y1="0" x2="1" y2="1">
            <stop offset="0" stop-color="#1f95da"/>
            <stop offset="0.5" stop-color="#1479bd"/>
            <stop offset="1" stop-color="#0b5d99"/>
          </linearGradient>
        </defs>
        <path d="M90,0 C30,300 440,360 405,660 L495,660 L495,0 Z" fill="url(#blueTone)"/>
      </svg>
      <div class="back-contact">
        <div class="agency-block">
          <div class="agency-name">Valmoric Agency LLC</div>
          <div>2480 Linden Crest Drive, Suite 410</div>
          <div>Houston, Texas, 77000</div>
        </div>
        <span class="contact-divider"></span>
        <ul class="contact-lines">
          <li><svg viewBox="0 0 10 10"><path d="M2 0.5 L3.6 0.5 L4.3 2.8 L3.2 3.7 Q4.2 5.9 6.3 6.8 L7.2 5.7 L9.5 6.4 L9.5 8 Q9.5 9.5 8 9.5 Q0.5 9 0.5 2 Q0.5 0.5 2 0.5 Z"/></svg>713-555-0148</li>
          <li><svg viewBox="0 0 10 10"><path d="M0.5 2 L9.5 2 L9.5 8 L0.5 8 Z M1.2 2.6 L5 5.4 L8.8 2.6" stroke="#5b5c60" stroke-width="0.7"/></svg>info@valmoriccorp.example</li>
          <li><svg viewBox="0 0 10 10"><circle cx="5" cy="5" r="4.5"/></svg>www.valmoriccorp.example</li>
        </ul>
      </div>
    </section>
    <section class="cover front-cover">
      <div class="brand-lockup">
        <span class="brand-square"></span>
        <span class="brand-name">Valmoric</span>
      </div>
      <div class="skyline-area" role="img" aria-label="Pale grey silhouette of the Houston, Texas skyline"></div>
    </section>
  </main>
</body>
</html>
```